Real Estate Investor needs awesome business card design

I invest in real estate, focused on multi-family properties, and I need a business card to hand out to potential partners. I prefer simple, clean designs, but it needs to stand out, so I'd like there to be a bit of red in the design as well.

It should include this information:

Front
Dallin Pecksworth
Real Estate Investor
Direct phone: 502-867-3394
Email: dallinhpecksworth@quillmail.example
Headshot (Picture), I've uploaded a few, just pick the one you think looks best with your design. You can remove the background from the headshot image if it looks better.

Back
The back of the card's design should flow and be congruent with the front. On the back I want to put an inspirational quote or question. There will be different ones depending on the card, so I'll need the original file so I can edit it in the end.

For now, use “The Pessimist Sees Difficulty In Every Opportunity. The Optimist Sees The Opportunity In Every Difficulty.” -Barnaby Ellsworth

Target Market(s)

Investors

Industry/Entity Type

Real Estate

Contact Information for Business Card

Front
Dallin Pecksworth
Real Estate Investor

Back
The back of the card's design should flow and be congruent with the front. On the back I want to put an inspirational quote or question. There will be different ones depending on the card, so I'll need the original file so I can edit it in the end. I've uploaded some EXAMPLES of business cards with quotes on them. Don't copy but feel free to use them as inspiration.

The design will be printed on "ZIB sized" business cards
1039 x 697 pixels
with rounded corners

Font styles to use
Serif
Decorative
Script

Colors
ec1f27

Requirements
Must have
• Headshot, name, and other information in it.
• 1039 x 697 pixels
• Rounded corners
• Clean design that pops. I'm open to see any color background, including black.
• Headshots can be located here: https://www.filecrate.example/sh/8kd2wq7mzt31hvx/BBQTXP4ruf9LmQ0KhcvWx7b?dl=0
Nice to have
• It would be awesome if the design included a personal signature or monogram, but if not I'll get a personal logo developed later and the card redesigned if I think it needs it.
Should not have
• Cluttered design

```html
<!DOCTYPE html>
<html lang="en">
<head>
<meta charset="utf-8">
<title>Dallin Pecksworth — Business Card</title>
<link rel="stylesheet" href="https://fonts.googleapis.com/css2?family=Noto+Serif:wght@400;700&family=Oswald:wght@500;600&family=Open+Sans:wght@400&display=swap">
<style>
  :root {
    --brand-red: #ec1f27;
    --card-black: #1b1b1d;
    --band-dark: #222224;
    --band-light: #2b2b2e;
    --text-white: #ffffff;
    --text-soft: #d9d9d9;
    --author-ink: #4a0d10;
    --scene-bg: #2a2b2e;
  }
  * { margin: 0; padding: 0; box-sizing: border-box; }
  html, body {
    width: 1200px;
    height: 900px;
    overflow: hidden;
    background: var(--scene-bg);
  }
  .sheet {
    width: 1200px;
    height: 900px;
    display: flex;
    align-items: center;
    justify-content: center;
    gap: 40px;
  }
  .card {
    position: relative;
    width: 520px;
    height: 349px;
    border-radius: 22px;
    overflow: hidden;
    box-shadow: 0 10px 30px rgba(0,0,0,.45);
  }

  /* Front */
  .card-front {
    background: var(--card-black);
  }
  .front-band {
    position: absolute;
    left: 0;
    width: 100%;
  }
  .front-band.upper { top: 0; height: 58px; background: var(--band-dark); }
  .front-band.lower { top: 200px; height: 38px; background: var(--band-dark); }
  .name-block {
    position: absolute;
    top: 28px;
    left: 26px;
    padding: 14px 20px 14px 18px;
    background: var(--band-light);
  }
  .name {
    font-family: "Noto Serif", serif;
    font-weight: 400;
    font-size: 23px;
    line-height: 1.1;
    color: var(--text-white);
    white-space: nowrap;
  }
  .name .surname { color: var(--brand-red); }
  .title {
    margin-top: 8px;
    font-family: "Noto Serif", serif;
    font-size: 9.5px;
    letter-spacing: .04em;
    text-transform: uppercase;
    color: var(--text-soft);
  }
  .headshot {
    position: absolute;
    right: 0;
    bottom: 0;
    width: 270px;
    height: 255px;
    background: radial-gradient(ellipse at 55% 35%, #c49a82 0%, #8a6656 28%, #2c3346 60%, rgba(27,27,29,0) 80%);
  }
  .contact {
    position: absolute;
    left: 20px;
    bottom: 26px;
    display: flex;
    flex-direction: column;
    gap: 6px;
    align-items: flex-end;
    width: 250px;
  }
  .contact-row {
    display: flex;
    align-items: center;
    gap: 8px;
  }
  .contact-text {
    font-family: "Noto Serif", serif;
    font-size: 10px;
    color: var(--text-white);
    white-space: nowrap;
  }
  .contact-icon {
    width: 28px;
    height: 28px;
    background: var(--brand-red);
    display: flex;
    align-items: center;
    justify-content: center;
    flex: none;
  }

  /* Back */
  .card-back {
    background: var(--brand-red);
  }
  .quote {
    position: absolute;
    top: 48px;
    left: 40px;
    transform: skewX(-8deg);
    font-family: "Oswald", sans-serif;
    font-weight: 600;
    font-size: 27px;
    line-height: 1.12;
    letter-spacing: .01em;
    text-transform: uppercase;
    color: var(--text-white);
  }
  .quote-mark { font-weight: 600; }
  .quote-author {
    position: absolute;
    top: 196px;
    left: 40px;
    font-family: "Open Sans", sans-serif;
    font-size: 11px;
    letter-spacing: .05em;
    text-transform: uppercase;
    color: var(--author-ink);
  }
</style>
</head>
<body>
<main class="sheet">
  <section class="card card-front" aria-label="Business card front">
    <div class="front-band upper"></div>
    <div class="front-band lower"></div>
    <div class="headshot" role="img" aria-label="Headshot of Dallin Pecksworth in a dark blazer and blue patterned shirt"></div>
    <div class="name-block">
      <h1 class="name">Dallin <span class="surname">Pecksworth</span></h1>
      <p class="title">Real Estate Investor</p>
    </div>
    <div class="contact">
      <div class="contact-row">
        <span class="contact-text">502-867-3394</span>
        <span class="contact-icon">
          <svg width="14" height="14" viewBox="0 0 24 24" aria-hidden="true"><path fill="#fff" d="M6.6 10.8c1.4 2.8 3.8 5.1 6.6 6.6l2.2-2.2c.3-.3.7-.4 1-.2 1.1.4 2.3.6 3.6.6.6 0 1 .4 1 1V20c0 .6-.4 1-1 1C10.6 21 3 13.4 3 4c0-.6.4-1 1-1h3.5c.6 0 1 .4 1 1 0 1.3.2 2.5.6 3.6.1.3 0 .7-.2 1z"/></svg>
        </span>
      </div>
      <div class="contact-row">
        <span class="contact-text">dallinhpecksworth@quillmail.example</span>
        <span class="contact-icon">
          <svg width="14" height="14" viewBox="0 0 24 24" aria-hidden="true"><rect x="3" y="6" width="18" height="12" fill="#fff"/><path d="M3 6l9 7 9-7" fill="none" stroke="#ec1f27" stroke-width="1.6"/></svg>
        </span>
      </div>
    </div>
  </section>

  <section class="card card-back" aria-label="Business card back">
    <blockquote class="quote">
      <span class="quote-mark">&ldquo;</span>The pessimist sees difficulty<br>
      in every opportunity.<br>
      The optimist sees the<br>
      opportunity in every difficulty.<span class="quote-mark">&rdquo;</span>
    </blockquote>
    <p class="quote-author">-Barnaby Ellsworth.</p>
  </section>
</main>
</body>
</html>
```